New Jar Label for Manuka Honey Company!

Hine Roa Honey, a Manuka Honey company from New Zealand is looking for a fresh & engaging label for our manuka honey jars.

Attached are some examples of label designs that we like, feel free to use the language/copy on these labels for inspiration/content/copy, but feel free to add your own creative spin if you have a great design idea!

LABEL DIMENSIONS: 1654mmx532mm

Label Must Include:
- MGO rating
- Made (or) Product of New Zealand
- Manuka Honey (can add extra text similar to attached examples)

Label Can Include:
- Badges: raw food, non gmo, bpa free, gluten free, halal etc
- anything you feel is appropriate

You can change the color of the logo(s) to Black, White, Silver or Gold.

Can you please include a mockup of your label design(s) on the supplied "Jar Mockup File". You can change the scene of the mockup if you like.

UPDATE:

Have decided on bee logo so please bo longer use the mountain logo for label mockups. Design(s) will need multiple color variations to represent the other MGO ratings, flavor combos and other honey types, other than manuka.

• Provide multiple designs for each honey type
Manuka Design
Spring Honey Design
MGO 100-1000 Design(s)
Wildflower Honey Design
Flavor Combo Honey Design

```html
<!DOCTYPE html>
<html lang="en">
<head>
<meta charset="utf-8">
<title>Hine Roa Honey – Manuka Honey Jar Label</title>
<link rel="stylesheet" href="https://fonts.googleapis.com/css2?family=Heebo:wght@400;500;700&family=Josefin+Sans:wght@400;600;700&family=Rosarivo&family=Montserrat:wght@700;800&family=Oxanium:wght@400&display=swap">
<style>
  :root {
    --ink: #000000;
    --white: #ffffff;
    --gold: #d9b13b;
    --gold-light: #f4d870;
    --gold-dark: #a27a1d;
    --gold-grad: linear-gradient(135deg, #a27a1d 0%, #f4d870 45%, #c79a2c 70%, #f0cf63 100%);
    --table-text: #111111;
  }
  * { box-sizing: border-box; margin: 0; padding: 0; }
  html, body { width: 1200px; height: 380px; overflow: hidden; background: var(--ink); }
  .label {
    position: relative; width: 1200px; height: 380px; background: var(--ink);
    color: var(--white); font-family: "Heebo", Arial, sans-serif; overflow: hidden;
  }
  .abs { position: absolute; }

  /* Left panel */
  .ingredients { left: 24px; top: 19px; width: 190px; font-size: 9.6px; line-height: 12px; }
  .ingredients strong { font-weight: 700; }
  .nutrition {
    left: 24px; top: 60px; width: 164px; height: 193px; background: var(--white);
    color: var(--table-text); padding: 2px 4px 0 4px; font-size: 7.6px;
  }
  .nutrition h2 {
    font-family: "Montserrat", Arial, sans-serif; font-weight: 800; font-size: 11.5px;
    text-align: center; border-bottom: 1px solid #000; padding-bottom: 1px;
  }
  .nutrition .serving { font-size: 6px; font-weight: 700; line-height: 7.6px; padding: 2px 0 3px; border-bottom: 3px solid #000; }
  .nutrition table { width: 100%; border-collapse: collapse; }
  .nutrition th { font-size: 5.8px; font-weight: 700; text-align: right; line-height: 6.6px; padding: 3px 0 2px; border-bottom: 1px solid #000; }
  .nutrition td { line-height: 12.1px; border-bottom: 0.6px solid #666; }
  .nutrition td.num { text-align: right; }
  .nutrition td.sub { padding-left: 14px; }
  .nutrition tr:last-child td { border-bottom: 3px solid #000; }
  .batch-info { left: 24px; top: 258px; font-size: 9.6px; line-height: 17.6px; }
  .storage { left: 136px; top: 354px; font-size: 8.6px; font-weight: 500; }

  /* Artwork placeholders */
  .art { position: absolute; }
  .comb-top-left { left: 237px; top: 0; width: 218px; height: 110px; background: linear-gradient(160deg, rgba(217,177,59,.28), rgba(217,177,59,.05)); }
  .flower-left { left: 296px; top: 115px; width: 94px; height: 90px; border-radius: 50%; background: radial-gradient(circle, rgba(244,216,112,.55), rgba(162,122,29,.2)); }
  .bee-path-left { left: 370px; top: 85px; width: 92px; height: 100px; background: linear-gradient(135deg, rgba(217,177,59,.25), rgba(217,177,59,.04)); border-radius: 40%; }
  .comb-top-right { left: 1030px; top: 0; width: 170px; height: 90px; background: linear-gradient(200deg, rgba(217,177,59,.28), rgba(217,177,59,.04)); }
  .flower-right { left: 820px; top: 200px; width: 66px; height: 62px; border-radius: 50%; background: radial-gradient(circle, rgba(244,216,112,.5), rgba(162,122,29,.18)); }
  .bee-path-right { left: 888px; top: 198px; width: 84px; height: 92px; background: linear-gradient(135deg, rgba(217,177,59,.22), rgba(217,177,59,.04)); border-radius: 40%; }
  .comb-bottom { left: 765px; top: 255px; width: 230px; height: 125px; background: linear-gradient(170deg, rgba(217,177,59,.06), rgba(217,177,59,.26)); }

  /* Centre panel */
  .brand {
    left: 400px; top: 31px; width: 400px; text-align: center;
    font-family: "Josefin Sans", Arial, sans-serif; font-weight: 400; font-size: 30px; letter-spacing: 5.5px;
  }
  .origin-claim {
    left: 440px; top: 163px; width: 120px; text-align: right;
    font-family: "Oxanium", Arial, sans-serif; font-size: 15px; line-height: 19px;
  }
  .rule { height: 1.5px; background: var(--gold-grad); }
  .rule-left { left: 444px; top: 205px; width: 116px; }
  .rule-right { left: 615px; top: 298px; width: 96px; }
  .product-name {
    font-family: "Josefin Sans", Arial, sans-serif; font-weight: 700; font-size: 43px; letter-spacing: 3px;
    background: var(--gold-grad); -webkit-background-clip: text; background-clip: text; color: transparent;
  }
  .product-manuka { left: 480px; top: 213px; }
  .product-honey { left: 548px; top: 255px; }
  .net-weight { left: 450px; top: 338px; width: 300px; text-align: center; font-family: "Oxanium", Arial, sans-serif; font-size: 17px; }

  /* Rating badges */
  .rating-badge { position: absolute; width: 54px; height: 62px; }
  .rating-badge svg { position: absolute; inset: 0; }
  .rating-badge span {
    position: absolute; inset: 0; display: flex; flex-direction: column; justify-content: center; align-items: center;
    font-family: "Montserrat", Arial, sans-serif; font-weight: 800; color: var(--ink); font-size: 16px; line-height: 16px;
  }
  .badge-umf { left: 721px; top: 288px; }
  .badge-mgo { left: 775px; top: 252px; }

  /* Right panel */
  .welcome { left: 969px; top: 56px; font-family: "Rosarivo", Georgia, serif; font-size: 16.5px; line-height: 20px; color: var(--gold); }
  .story { left: 969px; top: 102px; width: 220px; font-family: "Rosarivo", Georgia, serif; font-size: 10.4px; line-height: 12.6px; }
  .claims { left: 1014px; top: 180px; width: 120px; height: 80px; }
  .claim-text {
    position: absolute; width: 38px; text-align: center; font-family: "Montserrat", Arial, sans-serif;
    font-weight: 800; font-size: 7.6px; line-height: 8px; color: var(--ink);
  }
  .made-in { left: 1118px; top: 224px; font-size: 9.8px; font-weight: 500; line-height: 12.5px; }
  .distributor { left: 1053px; top: 271px; font-size: 7.6px; line-height: 11px; }
  .distributor .company { font-size: 10.4px; font-weight: 700; line-height: 13px; }
  .distributor .contact { font-size: 8.6px; line-height: 10.5px; }
  .distributor .contact b { font-weight: 700; }
  .website {
    left: 1043px; top: 323px; width: 170px; height: 18px; border-radius: 9px 0 0 9px; background: var(--gold-grad);
    color: var(--ink); font-size: 10px; font-weight: 700; line-height: 18px; padding-left: 10px;
  }
  .social { top: 351px; display: flex; align-items: center; gap: 3px; }
  .social .mark { width: 12px; height: 12px; border: 1px solid var(--white); border-radius: 2px; }
  .social .label-text { font-size: 5px; line-height: 6px; }
  .social .label-text b { display: block; font-size: 8.4px; line-height: 9px; font-weight: 700; }
  .social-one { left: 1057px; }
  .social-two { left: 1115px; }
</style>
</head>
<body>
<main class="label">

  <!-- Left panel -->
  <p class="abs ingredients"><strong>Ingredients:</strong> 100% South Island, NZ Honey, No Added Sugar, No artificial flavours, colors or preservatives.</p>

  <section class="abs nutrition">
    <h2>Nutrition Information</h2>
    <div class="serving">Servings per package: 13<br>Serving size : 8ml</div>
    <table>
      <tr><th></th><th>Avg. Quantity<br>per serve</th><th>Avg. Quantity<br>per 100g</th></tr>
      <tr><td>Energy</td><td class="num">148kJ</td><td class="num">1480kJ</td></tr>
      <tr><td>Protein</td><td class="num">0g</td><td class="num">0g</td></tr>
      <tr><td>Fat (Total)</td><td class="num">0g</td><td class="num">0g</td></tr>
      <tr><td class="sub">- Saturated</td><td class="num">0g</td><td class="num">0g</td></tr>
      <tr><td class="sub">-Trans</td><td class="num">0g</td><td class="num">0g</td></tr>
      <tr><td class="sub">- Polyunsaturated</td><td class="num">0g</td><td class="num">0g</td></tr>
      <tr><td class="sub">- Monounsaturated</td><td class="num">0g</td><td class="num">0g</td></tr>
      <tr><td>Coarbohydrate</td><td class="num">8.7g</td><td class="num">87g</td></tr>
      <tr><td class="sub">- Sugars</td><td class="num">8.1g</td><td class="num">81g</td></tr>
      <tr><td>Sodium</td><td class="num">0.7mg</td><td class="num">7mg</td></tr>
    </table>
  </section>

  <div class="abs batch-info">Pkg. Date :<br>Best Before :<br>Batch :</div>
  <p class="abs storage">Store below 20º C.</p>

  <!-- Decorative artwork areas -->
  <div class="art comb-top-left" role="img" aria-label="Gold outline honeycomb pattern"></div>
  <div class="art flower-left" role="img" aria-label="Gold line illustration of a manuka flower"></div>
  <div class="art bee-path-left" role="img" aria-label="Gold bee illustration with a dotted flight path"></div>
  <div class="art comb-top-right" role="img" aria-label="Gold outline honeycomb pattern"></div>
  <div class="art flower-right" role="img" aria-label="Gold line illustration of a manuka flower"></div>
  <div class="art bee-path-right" role="img" aria-label="Gold bee illustration with a dotted flight path"></div>
  <div class="art comb-bottom" role="img" aria-label="Gold outline honeycomb pattern"></div>

  <!-- Centre panel -->
  <h1 class="abs brand">HINE ROA HONEY</h1>
  <p class="abs origin-claim">100% Pure<br>New Zealand</p>
  <div class="abs rule rule-left"></div>
  <div class="abs product-name product-manuka">MANUKA</div>
  <div class="abs product-name product-honey">HONEY</div>
  <div class="abs rule rule-right"></div>
  <p class="abs net-weight">250 g (8.8 oz)</p>

  <div class="rating-badge badge-umf">
    <svg viewBox="0 0 54 62" aria-hidden="true"><defs><linearGradient id="gg1" x1="0" y1="0" x2="1" y2="1"><stop offset="0" stop-color="#a27a1d"/><stop offset=".45" stop-color="#f4d870"/><stop offset="1" stop-color="#c79a2c"/></linearGradient></defs><polygon points="27,0 54,15.5 54,46.5 27,62 0,46.5 0,15.5" fill="url(#gg1)"/></svg>
    <span>20+<br>UMF</span>
  </div>
  <div class="rating-badge badge-mgo">
    <svg viewBox="0 0 54 62" aria-hidden="true"><polygon points="27,0 54,15.5 54,46.5 27,62 0,46.5 0,15.5" fill="url(#gg1)"/></svg>
    <span>830+<br>MGO</span>
  </div>

  <!-- Right panel -->
  <h2 class="abs welcome">Welcome to<br>the world of good...</h2>
  <p class="abs story">Where bees and hives are nurtured and honey is kept in its most natural state. Where you'll benefit from the finest quality nutrition, traceable to its origin, pure to its core. Where focus and passion do a world of good.</p>

  <div class="abs claims">
    <svg width="120" height="80" viewBox="0 0 120 80" aria-hidden="true">
      <polygon points="19,0 38,10 38,32 19,42 0,32 0,10" fill="url(#gg1)"/>
      <polygon points="58,0 77,10 77,32 58,42 39,32 39,10" fill="url(#gg1)"/>
      <polygon points="97,0 116,10 116,32 97,42 78,32 78,10" fill="none" stroke="#d9b13b" stroke-width="0.8"/>
      <polygon points="39,36 58,46 58,68 39,78 20,68 20,46" fill="url(#gg1)"/>
      <polygon points="78,36 97,46 97,68 78,78 59,68 59,46" fill="url(#gg1)"/>
    </svg>
    <div class="claim-text" style="left:0;top:20px">NON<br>GMO</div>
    <div class="claim-text" style="left:39px;top:20px">GLUTEN<br>FREE</div>
    <div class="claim-text" style="left:20px;top:50px">BPA<br>FREE</div>
    <div class="claim-text" style="left:59px;top:55px">RAW<br>FOOD</div>
  </div>
  <p class="abs made-in">Product of<br>New Zealand</p>

  <div class="abs distributor">
    Marketed and Distributed by
    <div class="company">Company Name</div>
    <div class="contact">Address line will be here.<br>Tel : <b>+00 (0)0 000 0000</b></div>
  </div>
  <div class="abs website">www.website.com</div>

  <div class="abs social social-one"><span class="mark"></span><span class="label-text">Find us on<b>Buzzline</b></span></div>
  <div class="abs social social-two"><span class="mark"></span><span class="label-text">Find us on<b>Snapcomb</b></span></div>

</main>
</body>
</html>
```